Fernleaf Nutrition

we provide nutritional consulting for loss weight and changing food habits. The clinic is promoting the life healthy, as well as natural and balanced diets that help in the control weight and for the treatment to diseases.

Reason: Waiting some desings.

Reason: Waiting some designers

Reason: Waiting for changes.

Target Market(s)

Mostly women and men aged 30-55, both with overweight, obesity and problems with your food habits.

Industry/Entity Type

Weight

Font styles to use
Script

Colors
cadf82
ffc214
b868aa
f68d4d
0393ce
33b7a4
acd037
cbdf83
eaf2cf

Requirements
Must have
• lively and natural colors
logo that evokes healthy weight, concept of healthy natural food
Nice to have
• Slim fit image with a elegant and simple design
Should not have
• Preferably not used photograps, old-Style, Boring colors

```html
<!DOCTYPE html>
<html lang="en">
<head>
<meta charset="utf-8">
<title>Fernleaf Nutrition – Business Card</title>
<link href="https://fonts.googleapis.com/css2?family=Jura:wght@500;600&display=swap" rel="stylesheet">
<style>
  :root {
    --bg: #e4e4e4;
    --card: #ffffff;
    --blue: #0a86cf;
    --blue-light: #1fa6e0;
    --green: #5aa63c;
    --green-light: #b5d77a;
    --ink: #333333;
    --ink-soft: #444444;
  }
  * { box-sizing: border-box; margin: 0; padding: 0; }
  html, body {
    width: 1200px; height: 900px; overflow: hidden;
    background: var(--bg);
    font-family: "Jura", "Segoe UI", sans-serif;
  }
  .stage {
    width: 1200px; height: 900px;
    display: flex; align-items: center; justify-content: center;
  }
  .card {
    position: relative;
    width: 1000px; height: 570px;
    background: var(--card);
    box-shadow: 0 10px 30px rgba(0,0,0,0.15);
    overflow: hidden;
  }
  .card-swoosh { position: absolute; inset: 0; }
  .brand {
    position: absolute; left: 70px; top: 190px;
    display: flex; align-items: center; gap: 18px;
  }
  .brand-mark {
    width: 64px; height: 64px; border-radius: 50%;
    background: var(--green);
  }
  .brand-name {
    font-size: 48px; font-weight: 500; color: var(--blue-light);
    letter-spacing: 0.5px;
  }
  .contact-list {
    position: absolute; left: 90px; top: 325px;
    list-style: none;
  }
  .contact-item {
    display: flex; align-items: center; gap: 12px;
    font-size: 21px; font-weight: 500; color: var(--ink-soft);
    height: 36px;
  }
  .contact-icon {
    width: 22px; height: 22px; flex: none;
  }
  .person {
    position: absolute; right: 70px; top: 70px; text-align: right;
  }
  .person-name {
    font-size: 30px; font-weight: 600; color: var(--blue-light);
    letter-spacing: 2px; text-transform: uppercase;
  }
  .person-role {
    font-size: 20px; font-weight: 600; color: var(--ink);
    letter-spacing: 2px; text-transform: uppercase; margin-top: 4px;
  }
</style>
</head>
<body>
<main class="stage">
  <section class="card">
    <svg class="card-swoosh" viewBox="0 0 1000 570" aria-hidden="true">
      <path d="M420 570 C640 480 860 330 1000 180 L1000 260 C870 400 700 510 560 570 Z" fill="var(--blue)"/>
      <path d="M395 570 C620 475 845 320 1000 165" fill="none" stroke="var(--green)" stroke-width="9"/>
      <path d="M370 570 C560 480 730 380 830 300" fill="none" stroke="var(--green-light)" stroke-width="5"/>
    </svg>

    <div class="brand">
      <span class="brand-mark"></span>
      <span class="brand-name">Fernleaf Nutrition</span>
    </div>

    <ul class="contact-list">
      <li class="contact-item">
        <svg class="contact-icon" viewBox="0 0 22 22"><circle cx="11" cy="11" r="11" fill="var(--blue-light)"/><path d="M7 6 l2 0 l1 3 l-1.5 1 a7 7 0 0 0 3.5 3.5 l1 -1.5 l3 1 l0 2 a1 1 0 0 1 -1 1 a10 10 0 0 1 -9 -9 a1 1 0 0 1 1 -1z" fill="#fff"/></svg>
        010 555 0142
      </li>
      <li class="contact-item">
        <svg class="contact-icon" viewBox="0 0 22 22"><circle cx="11" cy="11" r="11" fill="var(--blue-light)"/><rect x="8" y="5" width="6" height="12" rx="1" fill="#fff"/></svg>
        010 555 0187
      </li>
      <li class="contact-item">
        <svg class="contact-icon" viewBox="0 0 22 22"><circle cx="11" cy="11" r="11" fill="var(--blue-light)"/><rect x="5.5" y="7" width="11" height="8" fill="#fff"/><path d="M5.5 7 l5.5 4.5 l5.5 -4.5" fill="none" stroke="var(--blue-light)" stroke-width="1.2"/></svg>
        hello@fernleafclinic.com
      </li>
      <li class="contact-item">
        <svg class="contact-icon" viewBox="0 0 22 22"><circle cx="11" cy="11" r="11" fill="var(--blue-light)"/><circle cx="11" cy="11" r="5.5" fill="none" stroke="#fff" stroke-width="1.3"/><path d="M5.5 11 h11 M11 5.5 v11" stroke="#fff" stroke-width="1.2"/></svg>
        www.fernleafclinic.com
      </li>
      <li class="contact-item">
        <svg class="contact-icon" viewBox="0 0 22 22"><circle cx="11" cy="11" r="11" fill="var(--blue-light)"/><path d="M11 17 C8 13 7 11.5 7 9.5 a4 4 0 0 1 8 0 c0 2 -1 3.5 -4 7.5z" fill="#fff"/><circle cx="11" cy="9.5" r="1.4" fill="var(--blue-light)"/></svg>
        24 Orchard Lane, 5th Floor, Brookfield
      </li>
    </ul>

    <div class="person">
      <p class="person-name">Daniel Reyes</p>
      <p class="person-role">Financial Advisor</p>
    </div>
  </section>
</main>
</body>
</html>
```